THE HOMESTEAD LEDGER
STATIONARY, ENVELOPES, FLYERS, BUSINESS CARDS
Project: THE HOMESTEAD LEDGER
THE HOMESTEAD LEDGER - Real Estate
Creative Brief
Professional
MALCOLM J. VANTREASE
PRINCIPAL BROKER
518 WILLOWCREST DRIVE ELIZABETHTOWN, KENTUCKY 42701
malcolmvantrease@quillmail.example
FRONT SIDE DESIGN AND/OR LOGO WITH INDIVIDUAL INFORMATION AND AREA FOR INDIVIDUAL PICTURE.
AT LEAST "THE HOMESTEAD LEDGER" LOGO. OPEN TO OTHER DESIGN AND/OR BORDERS WITH IT.

```html
<!DOCTYPE html>
<html lang="en">
<head>
<meta charset="utf-8">
<title>The Homestead Ledger — Stationery Set</title>
<link href="https://fonts.googleapis.com/css2?family=Cormorant+Garamond:wght@500;600&display=swap" rel="stylesheet">
<style>
  :root{
    --backdrop:#4a3326;
    --paper:#ffffff;
    --olive-dark:#8b8758;
    --olive-mid:#aaa67a;
    --olive-light:#d2cfae;
    --silver:#c9c9c9;
    --ink:#5c5a4a;
    --ink-light:#f3f1e6;
    --ghost:#ecebe5;
    --serif:"Cormorant Garamond", Georgia, serif;
  }
  *{box-sizing:border-box;margin:0;padding:0}
  html,body{width:1200px;height:732px;overflow:hidden}
  body{background:var(--backdrop);font-family:var(--serif);position:relative}
  .piece{position:absolute;background:var(--paper);box-shadow:0 4px 14px rgba(0,0,0,.35);overflow:hidden}
  .piece svg.art{position:absolute;inset:0;width:100%;height:100%}
  .brand{position:absolute;font-weight:600;letter-spacing:.08em;line-height:1.05;white-space:nowrap;display:flex;align-items:center;gap:5px}
  .brand .mark{display:inline-block;flex:none;background:currentColor}
  .contact{position:absolute;color:var(--ink-light);font-weight:500;line-height:1.35;letter-spacing:.05em;text-transform:uppercase;white-space:nowrap}

  /* Letterhead */
  .letterhead{left:139px;top:43px;width:444px;height:648px}
  .letterhead .brand{left:40px;top:26px;font-size:14px;color:var(--ink-light)}
  .letterhead .brand .mark{width:8px;height:8px}
  .letterhead .contact{left:282px;top:16px;font-size:6.5px}
  .letterhead .watermark{left:0;right:0;top:296px;justify-content:center;text-align:center;font-size:32px;color:var(--ghost)}
  .letterhead .footer{position:absolute;left:0;right:0;bottom:7px;text-align:center;font-size:6px;color:var(--ink-light);letter-spacing:.08em}

  /* Business cards */
  .card{top:77px;width:161px;height:96px}
  .card-front{left:667px}
  .card-front .brand{left:10px;top:11px;font-size:7px;color:var(--ink)}
  .card-front .brand .mark{width:5px;height:5px}
  .card-front .photo{position:absolute;left:101px;top:14px;width:41px;height:58px;background:linear-gradient(#f2f1ea,#dcdacb);border:1px solid var(--silver)}
  .card-front .person{position:absolute;left:10px;top:36px;font-size:5.5px;color:var(--ink);letter-spacing:.05em;line-height:1.4}
  .card-back{left:833px}
  .card-back .brand{left:48px;top:22px;font-size:7.5px;color:var(--ink-light)}
  .card-back .brand .mark{width:5px;height:5px}
  .card-back .contact{left:48px;top:48px;font-size:4.8px}

  /* Envelope */
  .envelope{left:605px;top:211px;width:523px;height:442px}
  .envelope .brand{left:60px;top:18px;font-size:12px;color:var(--ink)}
  .envelope .brand .mark{width:7px;height:7px}
  .envelope .contact{left:0;right:0;top:168px;text-align:center;font-size:6px}
  .envelope .watermark{left:0;right:0;top:266px;justify-content:center;text-align:center;font-size:17px;color:rgba(255,255,255,.24)}
</style>
</head>
<body>

<section class="piece letterhead" aria-label="Letterhead">
  <svg class="art" viewBox="0 0 444 648" preserveAspectRatio="none" aria-hidden="true">
    <defs>
      <linearGradient id="lhBand" x1="0" y1="0" x2="1" y2="0">
        <stop offset="0" stop-color="var(--olive-dark)"/>
        <stop offset=".55" stop-color="var(--olive-light)"/>
        <stop offset="1" stop-color="var(--olive-mid)"/>
      </linearGradient>
    </defs>
    <path d="M0 0H444V52C380 48 330 64 260 82C180 102 80 98 0 78Z" fill="url(#lhBand)"/>
    <path d="M0 82C80 102 180 106 260 86C330 68 380 54 444 56" fill="none" stroke="var(--silver)" stroke-width="2.5"/>
    <rect x="0" y="610" width="444" height="38" fill="url(#lhBand)"/>
    <line x1="0" y1="608" x2="444" y2="608" stroke="var(--silver)" stroke-width="2"/>
  </svg>
  <div class="brand"><span class="mark"></span><span>THE HOMESTEAD<br>LEDGER</span></div>
  <div class="contact">518 Willowcrest Drive<br>Elizabethtown, Kentucky 42701<br>(270) 555-0148</div>
  <div class="brand watermark"><span>THE HOMESTEAD<br>LEDGER</span></div>
  <div class="footer">malcolmvantrease@quillmail.example · www.homesteadledger.example</div>
</section>

<section class="piece card card-front" aria-label="Business card front">
  <svg class="art" viewBox="0 0 161 96" preserveAspectRatio="none" aria-hidden="true">
    <path d="M0 80C50 72 110 90 161 78V96H0Z" fill="var(--olive-mid)"/>
  </svg>
  <div class="brand"><span class="mark"></span><span>THE HOMESTEAD<br>LEDGER</span></div>
  <div class="person">MALCOLM J. VANTREASE<br>PRINCIPAL BROKER</div>
  <div class="photo" role="img" aria-label="Space for agent portrait"></div>
</section>

<section class="piece card card-back" aria-label="Business card back">
  <svg class="art" viewBox="0 0 161 96" preserveAspectRatio="none" aria-hidden="true">
    <defs>
      <linearGradient id="cardBand" x1="0" y1="0" x2="1" y2="1">
        <stop offset="0" stop-color="var(--olive-light)"/>
        <stop offset="1" stop-color="var(--olive-dark)"/>
      </linearGradient>
    </defs>
    <rect width="161" height="96" fill="url(#cardBand)"/>
  </svg>
  <div class="brand"><span class="mark"></span><span>THE HOMESTEAD<br>LEDGER</span></div>
  <div class="contact">518 Willowcrest Drive<br>Elizabethtown, KY 42701<br>(270) 555-0148</div>
</section>

<section class="piece envelope" aria-label="Envelope">
  <svg class="art" viewBox="0 0 523 442" preserveAspectRatio="none" aria-hidden="true">
    <defs>
      <linearGradient id="envBand" x1="0" y1="0" x2="1" y2="0">
        <stop offset="0" stop-color="var(--olive-dark)"/>
        <stop offset=".5" stop-color="var(--olive-light)"/>
        <stop offset="1" stop-color="var(--olive-mid)"/>
      </linearGradient>
    </defs>
    <path d="M0 150C140 140 330 176 523 130V200C360 224 190 196 0 214Z" fill="url(#envBand)"/>
    <path d="M0 214C190 196 360 226 523 202" fill="none" stroke="var(--silver)" stroke-width="2"/>
    <line x1="0" y1="222" x2="523" y2="222" stroke="#e2e2e2" stroke-width="1"/>
    <path d="M17 226C200 250 350 210 506 226V330C506 370 480 378 450 378H75C40 378 17 370 17 330Z" fill="url(#envBand)"/>
    <path d="M17 226C200 250 350 210 506 226" fill="none" stroke="var(--silver)" stroke-width="2"/>
  </svg>
  <div class="brand"><span class="mark"></span><span>THE HOMESTEAD<br>LEDGER</span></div>
  <div class="contact">518 Willowcrest Drive · Elizabethtown, Kentucky 42701 · (270) 555-0148</div>
  <div class="brand watermark"><span>THE HOMESTEAD<br>LEDGER</span></div>
</section>

</body>
</html>
```